TelvaLaw a fully remote and fully bilingual law firm for the Florida injured

1. Can you describe what your company does?- a solo lawyer practice in Florida, D.C., and soon in NY. I offer services for auto accidents, negligence, boat accident, motorcycle accident, insurance claims, premises liability, and things of the like.

2. Who are your target customers for the website? Drivers, passengers, pedestrians involved in accidents where they were injured and need help making a claim against the other vehicle or insurance company- throughout the entire state of Florida, but primarily in greater central florida area for english speaking and latino community offering a 100% bilingual services ENGLISH/SPANISH and 100% remote, where I wont make clients come to an office ever, and will private online meetings, signing portals, and all to have it efficient for clients benefit.

3. Do you have an existing domain name / website address? yes, telvalaw.com through google workspace. i need help in getting in brought to you so you can handle it please.

4. In addition to a Home Page, which other pages / sections would you like your website to have:
About Us
Contact Us
Products / Services
Office / Mailing Address
Testimonials / Reviews
FAQs
Terms and Conditions
Any other page / section you would like- DO EVERYTHING IN BOTH LANGUAGES- ENGLISH AND SPANISH
I want the page to have a way for people to calendar appts with me. and also
to make transactions - accepting all methods of payment

For each of the pages / sections you’d like to have, please provide the text (and images, if available) you would like to include.

5. Which of the below are features and functionalities your website will need:
Image Gallery
Videos
Contact Form
Mailing List
Maps
FAQs
Accepting payments / donations
6. Please provide the URLs for the social media profiles you'd like to link to the website. I have none, I am just starting, I actually want to have the online presence ready before my official launch.

Target Market(s)

Injured individuals by the negligent act of another in Florida

Industry/Entity Type

LAWYER/ AUTO ACCIDENT/NEGLIGENCE/ PREMISES LIABILITY/ CIVIL LAW

Coding

Coded - Design and coding required

Number of Pages Required

1 page

Requirements
Must have
• bilingual ENGLISH and SPANISH; a button for people to calendar appointments with me; accept payments, and to be able to integrate with major software like docusign, adobe, etc since I need to integrate under the fully remote platform
Nice to have
• look at my logo from markforge.com it has the Telvarique Law and TelvaLaw.com together.. I have the telvalaw.com domain from google. need you guys to help integrate that too , meaning to be able to use that domain for my website.

```html
<!DOCTYPE html>
<html lang="en">
<head>
<meta charset="utf-8">
<title>TelvaLaw – Homepage Concepts</title>
<link href="https://fonts.googleapis.com/css2?family=Kaushan+Script&family=Poppins:wght@400;500;600&family=Oswald:wght@500&family=Open+Sans:ital,wght@0,400;0,600;1,400&display=block" rel="stylesheet">
<style>
:root{
  --board:#eeeeef;
  --tan:#c4976a;
  --black:#000;
  --white:#fff;
  --light:#f2f2f2;
  --panel:#e6e6e6;
  --ink:#222;
  --muted:#666;
  --line:#dcdcdc;
  --sky-top:#5d6b86;
  --sky-mid:#8a8fa2;
  --sky-low:#b68a73;
  --water:#3a4254;
}
*{box-sizing:border-box;margin:0;padding:0}
html,body{width:769px;height:1200px;overflow:hidden}
body{background:var(--board);font-family:"Open Sans",Arial,sans-serif;color:var(--ink);position:relative}

.page{position:absolute;top:36px;width:270px;background:var(--white);box-shadow:0 2px 10px rgba(0,0,0,.08)}
.page--rounded{left:77px}
.page--condensed{left:422px;width:271px}
.section{position:relative;width:100%;overflow:hidden}
.abs{position:absolute}

.heading{font-family:"Poppins",sans-serif;font-weight:500;color:var(--ink)}
.page--condensed .heading{font-family:"Oswald",sans-serif;text-transform:uppercase;letter-spacing:.1px}

.btn{position:absolute;background:var(--tan);color:var(--white);border-radius:7px;font-family:"Poppins",sans-serif;font-weight:500;font-size:3.6px;display:flex;align-items:center;justify-content:center;letter-spacing:.1px;text-transform:uppercase;white-space:nowrap}
.page--condensed .btn{font-family:"Open Sans",sans-serif}

/* hero */
.hero{height:166px;background:linear-gradient(180deg,var(--sky-top) 0%,var(--sky-mid) 45%,var(--sky-low) 70%,var(--water) 100%)}
.brand{left:24px;top:3px;display:flex;flex-direction:column;align-items:center;gap:3px}
.brand__dot{width:16px;height:16px;border-radius:50%;border:1px solid var(--white)}
.brand__name{font-family:"Oswald",sans-serif;font-weight:500;font-size:4.6px;letter-spacing:1.4px;color:var(--white);text-transform:uppercase;white-space:nowrap}
.topbar{right:25px;top:8px;font-size:3.7px;color:var(--white);display:flex;gap:4px;white-space:nowrap}
.nav{right:25px;top:18px;font-size:3.9px;color:var(--white);display:flex;gap:5px;white-space:nowrap}
.hero__title{left:24px;top:44px;font-size:17px;color:var(--white);font-weight:500;white-space:nowrap}
.page--condensed .hero__title{font-size:18px;top:44px}
.hero__sub{left:25px;top:69px;font-size:4.8px;color:var(--white);white-space:nowrap}
.hero .btn{left:25px;top:82px;width:72px;height:12.5px}

/* about */
.about{height:136px;background:var(--light)}
.about__photo{left:0;top:0;width:135px;height:136px;background:linear-gradient(160deg,#e9eaee 0%,#d3d6de 55%,#5a6fa8 100%)}
.about__hi{left:136px;top:13px;font-family:"Kaushan Script",cursive;font-size:16px;line-height:20px;color:var(--black);white-space:nowrap}
.about__name{left:160px;top:36px;font-size:9.5px;white-space:nowrap}
.about__text{left:137px;top:58px;width:110px;font-size:3.5px;line-height:6px;color:var(--muted)}
.about .btn{left:137px;top:104px;width:39px;height:12px}

/* services */
.services{height:212px;background:var(--white)}
.services__title{width:100%;text-align:center;top:17px;font-size:10px}
.grid{left:25px;top:39px;width:219px;display:grid;grid-template-columns:repeat(3,1fr);grid-template-rows:84px 89px}
.card{position:relative;text-align:center;border-right:.5px solid var(--line)}
.card:nth-child(3n){border-right:none}
.card:nth-child(-n+3){border-bottom:.5px solid var(--line)}
.card__icon{position:absolute;left:50%;top:8px;width:30px;height:22px;margin-left:-15px;background:linear-gradient(135deg,#e3e3e3,#d1bca6);border-radius:2px}
.card__title{position:absolute;top:36px;width:100%;font-size:4.6px;font-family:"Poppins",sans-serif;font-weight:500}
.page--condensed .card__title{font-family:"Oswald",sans-serif;text-transform:uppercase}
.card__text{position:absolute;top:45px;left:5px;right:5px;font-size:3.3px;line-height:5.7px;color:var(--muted)}
.card__go{position:absolute;left:50%;top:67px;margin-left:-4px;width:8px;height:8px}

/* remote */
.remote{height:170px;background:var(--light)}
.remote__card{left:25px;top:20px;width:219px;height:129px;display:flex}
.remote__body{position:relative;width:110px;height:100%;background:var(--black);color:var(--white)}
.remote__photo{width:109px;height:100%;background:linear-gradient(150deg,#ececec 0%,#c7c2bb 45%,#5d7290 100%)}
.remote__title{left:12px;top:11px;font-size:10px;color:var(--white);white-space:nowrap}
.remote__text{left:12px;top:28px;width:90px;font-size:3.4px;line-height:6px}
.feature{left:12px;display:flex;align-items:center;gap:5px;font-size:4.8px;line-height:6px}
.feature__ring{width:21px;height:21px;border-radius:50%;border:.6px solid #777;display:flex;align-items:center;justify-content:center}
.remote .btn{left:12px;top:106px;width:39px;height:12px}

/* reviews */
.reviews{height:176px;background:var(--white)}
.reviews__title{width:100%;text-align:center;top:16px;font-size:10px}
.reviews__quote{left:56px;top:39px;width:157px;text-align:center;font-style:italic;font-size:3.7px;line-height:7px;color:#444}
.reviews__name{width:100%;text-align:center;top:76px;font-size:4.6px}
.reviews__video{left:83px;top:90px;width:102px;height:67px;background:linear-gradient(110deg,#cdd3c4 0%,#8e8578 50%,#2b2b2b 75%,#b9b9b9 100%);box-shadow:0 3px 8px rgba(0,0,0,.12)}
.play{left:50%;top:50%;width:10px;height:10px;margin:-5px 0 0 -5px;border-radius:50%;background:var(--black)}
.arrow{top:120px;width:9px;height:9px}

/* contact */
.contact{height:166px;background:var(--light)}
.contact__card{left:25px;top:21px;width:219px;height:122px;display:flex}
.contact__map{width:82px;height:100%;background:linear-gradient(160deg,#f7f5f2 0%,#d9c7b4 50%,#b09a85 100%)}
.contact__form{position:relative;flex:1;background:var(--panel)}
.contact__title{left:10px;top:10px;font-size:10px;white-space:nowrap}
.field{position:absolute;background:var(--white);border:.5px solid #d0d0d0;font-size:3.3px;color:#555;padding:3px 4px}
.contact .btn{left:10px;top:97px;width:27px;height:13px}

/* footer */
.footer{height:101px;background:var(--black);color:var(--white)}
.footer__mark{left:56px;top:14px;width:33px;height:33px;border-radius:50%;border:1px solid var(--white)}
.footer__name{left:24px;top:55px;font-family:"Oswald",sans-serif;font-weight:500;font-size:9px;letter-spacing:2.6px;text-transform:uppercase;white-space:nowrap}
.footer__col{top:14px;font-size:3.6px;line-height:6.7px}
.footer__col h4{font-family:"Poppins",sans-serif;font-weight:500;font-size:4.4px;margin-bottom:3px}
.contact-row{display:flex;align-items:center;gap:4px;margin-bottom:3px;white-space:nowrap}
.footer__rule{left:25px;top:78px;width:219px;height:.5px;background:#444}
.footer__copy{left:25px;top:87px;font-size:3.4px}
.social{top:85px;width:9px;height:9px;border-radius:50%;border:.6px solid var(--tan)}
</style>
</head>
<body>

<!-- ========== Concept A ========== -->
<main class="page page--rounded">
  <section class="section hero" role="img" aria-label="City skyline with river bridge at dusk">
    <div class="abs brand"><span class="brand__dot"></span><span class="brand__name">Telvarique Law</span></div>
    <div class="abs topbar"><span>✉ Email: info@telvalaw.com</span><span>☎ Call: 1 800 555 0142</span><span>EN / ES</span></div>
    <nav class="abs nav"><span>About Us</span><span>Contact Us</span><span>Services</span><span>Mailing Address</span><span>Testimonials</span><span>FAQs</span></nav>
    <h1 class="abs heading hero__title">TelvaLaw</h1>
    <p class="abs hero__sub">A solo lawyer practice in Florida, D.C., and soon in NY.</p>
    <a class="btn">▦ Book an appointment</a>
  </section>

  <section class="section about">
    <div class="abs about__photo" role="img" aria-label="Portrait of the attorney in a blue suit"></div>
    <p class="abs about__hi">Hi I am</p>
    <h2 class="abs heading about__name">Daniel Arvento</h2>
    <p class="abs about__text">Nemo enim ipsam voluptatem quia voluptas sit aspernatur aut odit aut fugit, sed quia consequuntur magni dolores eos qui ratione voluptatem sequi nesciunt. Neque porro quisquam est, qui dolorem ipsum quia dolor sit amet, consectetur, adipisci velit, sed quia non numquam eius modi tempora incidunt ut labore dolore magnam aliquam quaerat voluptatem.</p>
    <a class="btn">Contact us</a>
  </section>

  <section class="section services">
    <h2 class="abs heading services__title">I offer services</h2>
    <div class="abs grid">
      <div class="card"><div class="card__icon" role="img" aria-label="Car crash icon"></div><h3 class="card__title">Auto accidents</h3><p class="card__text">Nemo enim ipsam voluptatem quia voluptas sit aspernatur aut odit aut fugi sed quia consequu.</p><svg class="card__go" viewBox="0 0 16 16"><circle cx="8" cy="8" r="7.3" fill="none" stroke="#c4976a" stroke-width=".9"/><path d="M7 5l3 3-3 3" fill="none" stroke="#c4976a" stroke-width=".9"/></svg></div>
      <div class="card"><div class="card__icon" role="img" aria-label="Person with warning sign icon"></div><h3 class="card__title">Negligence</h3><p class="card__text">Nemo enim ipsam voluptatem quia voluptas sit aspernatur aut odit aut fugi sed quia consequu.</p><svg class="card__go" viewBox="0 0 16 16"><circle cx="8" cy="8" r="7.3" fill="none" stroke="#c4976a" stroke-width=".9"/><path d="M7 5l3 3-3 3" fill="none" stroke="#c4976a" stroke-width=".9"/></svg></div>
      <div class="card"><div class="card__icon" role="img" aria-label="Capsized boat icon"></div><h3 class="card__title">Boat accident</h3><p class="card__text">Nemo enim ipsam voluptatem quia voluptas sit aspernatur aut odit aut fugi sed quia consequu.</p><svg class="card__go" viewBox="0 0 16 16"><circle cx="8" cy="8" r="7.3" fill="none" stroke="#c4976a" stroke-width=".9"/><path d="M7 5l3 3-3 3" fill="none" stroke="#c4976a" stroke-width=".9"/></svg></div>
      <div class="card"><div class="card__icon" role="img" aria-label="Motorcycle collision icon"></div><h3 class="card__title">Motorcycle accident</h3><p class="card__text">Nemo enim ipsam voluptatem quia voluptas sit aspernatur aut odit aut fugi sed quia consequu.</p><svg class="card__go" viewBox="0 0 16 16"><circle cx="8" cy="8" r="7.3" fill="none" stroke="#c4976a" stroke-width=".9"/><path d="M7 5l3 3-3 3" fill="none" stroke="#c4976a" stroke-width=".9"/></svg></div>
      <div class="card"><div class="card__icon" role="img" aria-label="Insurance document icon"></div><h3 class="card__title">Insurance claims</h3><p class="card__text">Nemo enim ipsam voluptatem quia voluptas sit aspernatur aut odit aut fugi sed quia consequu.</p><svg class="card__go" viewBox="0 0 16 16"><circle cx="8" cy="8" r="7.3" fill="none" stroke="#c4976a" stroke-width=".9"/><path d="M7 5l3 3-3 3" fill="none" stroke="#c4976a" stroke-width=".9"/></svg></div>
      <div class="card"><div class="card__icon" role="img" aria-label="Hand holding money icon"></div><h3 class="card__title">Premises liability</h3><p class="card__text">Nemo enim ipsam voluptatem quia voluptas sit aspernatur aut odit aut fugi sed quia consequu.</p><svg class="card__go" viewBox="0 0 16 16"><circle cx="8" cy="8" r="7.3" fill="none" stroke="#c4976a" stroke-width=".9"/><path d="M7 5l3 3-3 3" fill="none" stroke="#c4976a" stroke-width=".9"/></svg></div>
    </div>
  </section>

  <section class="section remote">
    <div class="abs remote__card">
      <div class="remote__body">
        <h2 class="abs heading remote__title">100% Remote</h2>
        <p class="abs remote__text">Jma veniam, quis nostrum exercitationem der ulm corporis susc ut aliquid ex ea commodi consdeequ atu saum iure reprehenderit.</p>
        <div class="abs feature" style="top:53px"><span class="feature__ring"><svg width="9" height="7" viewBox="0 0 18 14"><rect x="3" y="1" width="12" height="8" fill="none" stroke="#fff" stroke-width="1.4"/><path d="M1 12h16" stroke="#fff" stroke-width="1.6"/></svg></span><span>Private<br>online meetings</span></div>
        <div class="abs feature" style="top:78px"><span class="feature__ring"><svg width="8" height="8" viewBox="0 0 16 16"><rect x="1.5" y="3" width="11" height="11" rx="1.5" fill="none" stroke="#fff" stroke-width="1.4"/><path d="M6 10l1-3 6-6 2 2-6 6z" fill="none" stroke="#fff" stroke-width="1.4"/></svg></span><span>Signing<br>portals</span></div>
        <a class="btn">Contact us</a>
      </div>
      <div class="remote__photo" role="img" aria-label="Woman working on a laptop"></div>
    </div>
  </section>

  <section class="section reviews">
    <h2 class="abs heading reviews__title">Client Reviews</h2>
    <p class="abs reviews__quote">“ Lorem ipsum dolor sit amet, consectetur adipiscing elit, sed do eiusmod tempor incidi dunt ut labore et dolore magna aliqua. Ut enim ad minim veniam, quis nostrud exercita tion ullamco laboris nisi ut aliquip ex ea commodo consequat. Duis aute irure dolor in reprehenderit in voluptate velit esse cillum dolore eu fug ”</p>
    <p class="abs reviews__name">- LIORA</p>
    <svg class="abs arrow" style="left:67px" viewBox="0 0 16 16"><circle cx="8" cy="8" r="7.3" fill="none" stroke="#c4976a" stroke-width=".9"/><path d="M9 5L6 8l3 3" fill="none" stroke="#c4976a" stroke-width=".9"/></svg>
    <svg class="abs arrow" style="left:193px" viewBox="0 0 16 16"><circle cx="8" cy="8" r="7.3" fill="none" stroke="#c4976a" stroke-width=".9"/><path d="M7 5l3 3-3 3" fill="none" stroke="#c4976a" stroke-width=".9"/></svg>
    <div class="abs reviews__video" role="img" aria-label="Video testimonial from a client">
      <svg class="abs play" viewBox="0 0 20 20"><circle cx="10" cy="10" r="10" fill="#000"/><path d="M8 6l6 4-6 4z" fill="#fff"/></svg>
    </div>
  </section>

  <section class="section contact">
    <div class="abs contact__card">
      <div class="contact__map" role="img" aria-label="Map of Florida"></div>
      <form class="contact__form">
        <h2 class="abs heading contact__title">Get In Touch</h2>
        <div class="field" style="left:10px;top:31px;width:58px;height:10px">First Name</div>
        <div class="field" style="left:71px;top:31px;width:58px;height:10px">Last Name</div>
        <div class="field" style="left:10px;top:46px;width:58px;height:10px">Email</div>
        <div class="field" style="left:71px;top:46px;width:58px;height:10px">Phone no.</div>
        <div class="field" style="left:10px;top:61px;width:119px;height:29px">Message</div>
        <a class="btn">Send</a>
      </form>
    </div>
  </section>

  <footer class="section footer">
    <span class="abs footer__mark"></span>
    <span class="abs footer__name">Telvarique Law</span>
    <div class="abs footer__col" style="left:148px"><h4>Quick Links</h4>Home<br>About Us<br>Contact Us<br>Services<br>Mailing Address<br>Testimonials<br>FAQs</div>
    <div class="abs footer__col" style="left:203px"><h4>Contact Info</h4>
      <div class="contact-row"><svg width="4" height="5" viewBox="0 0 8 10"><path d="M4 0a3.5 3.5 0 0 0-3.5 3.5C.5 6 4 10 4 10s3.5-4 3.5-6.5A3.5 3.5 0 0 0 4 0z" fill="#c4976a"/></svg>Florida, D.C</div>
      <div class="contact-row"><svg width="4" height="4" viewBox="0 0 10 10"><path d="M2 0l2 2.5-1 1.5a6 6 0 0 0 3 3l1.5-1L10 8l-1.5 2C4 10 0 6 0 1.5z" fill="#c4976a"/></svg>1 800 555 0142</div>
      <div class="contact-row"><svg width="5" height="4" viewBox="0 0 10 7"><rect width="10" height="7" fill="#c4976a"/><path d="M0 0l5 4 5-4" fill="none" stroke="#000" stroke-width=".8"/></svg>info@telvalaw.com</div>
    </div>
    <span class="abs footer__rule"></span>
    <p class="abs footer__copy">© Copyright 2025, TelvaLaw. All rights reserved.</p>
    <span class="abs social" style="left:223px"></span>
    <span class="abs social" style="left:235px"></span>
  </footer>
</main>

<!-- ========== Concept B ========== -->
<main class="page page--condensed">
  <section class="section hero" style="height:160px" role="img" aria-label="City skyline with river bridge at dusk">
    <div class="abs brand"><span class="brand__dot"></span><span class="brand__name">Telvarique Law</span></div>
    <div class="abs topbar"><span>✉ Email: info@telvalaw.com</span><span>☎ Call: 1 800 555 0142</span><span>EN / ES</span></div>
    <nav class="abs nav"><span>About Us</span><span>Contact Us</span><span>Services</span><span>Mailing Address</span><span>Testimonials</span><span>FAQs</span></nav>
    <h1 class="abs heading hero__title">TelvaLaw</h1>
    <p class="abs hero__sub">A solo lawyer practice in Florida, D.C., and soon in NY.</p>
    <a class="btn">▦ Book an appointment</a>
  </section>

  <section class="section about">
    <div class="abs about__photo" role="img" aria-label="Portrait of the attorney in a blue suit"></div>
    <p class="abs about__hi">Hi I am</p>
    <h2 class="abs heading about__name">Daniel Arvento</h2>
    <p class="abs about__text">Nemo enim ipsam voluptatem quia voluptas sit aspernatur aut odit aut fugit, sed quia consequuntur magni dolores eos qui ratione voluptatem sequi nesciunt. Neque porro quisquam est, qui dolorem ipsum quia dolor sit amet, consectetur, adipisci velit, sed quia non numquam eius modi tempora incidunt ut labore dolore magnam aliquam quaerat voluptatem.</p>
    <a class="btn">Contact us</a>
  </section>

  <section class="section services">
    <h2 class="abs heading services__title">I offer services</h2>
    <div class="abs grid">
      <div class="card"><div class="card__icon" role="img" aria-label="Car crash icon"></div><h3 class="card__title">Auto accidents</h3><p class="card__text">Nemo enim ipsam voluptatem quia voluptas sit aspernatur aut odit aut fugi sed quia consequu.</p><svg class="card__go" viewBox="0 0 16 16"><circle cx="8" cy="8" r="7.3" fill="none" stroke="#c4976a" stroke-width=".9"/><path d="M7 5l3 3-3 3" fill="none" stroke="#c4976a" stroke-width=".9"/></svg></div>
      <div class="card"><div class="card__icon" role="img" aria-label="Person with warning sign icon"></div><h3 class="card__title">Negligence</h3><p class="card__text">Nemo enim ipsam voluptatem quia voluptas sit aspernatur aut odit aut fugi sed quia consequu.</p><svg class="card__go" viewBox="0 0 16 16"><circle cx="8" cy="8" r="7.3" fill="none" stroke="#c4976a" stroke-width=".9"/><path d="M7 5l3 3-3 3" fill="none" stroke="#c4976a" stroke-width=".9"/></svg></div>
      <div class="card"><div class="card__icon" role="img" aria-label="Capsized boat icon"></div><h3 class="card__title">Boat accident</h3><p class="card__text">Nemo enim ipsam voluptatem quia voluptas sit aspernatur aut odit aut fugi sed quia consequu.</p><svg class="card__go" viewBox="0 0 16 16"><circle cx="8" cy="8" r="7.3" fill="none" stroke="#c4976a" stroke-width=".9"/><path d="M7 5l3 3-3 3" fill="none" stroke="#c4976a" stroke-width=".9"/></svg></div>
      <div class="card"><div class="card__icon" role="img" aria-label="Motorcycle collision icon"></div><h3 class="card__title">Motorcycle accident</h3><p class="card__text">Nemo enim ipsam voluptatem quia voluptas sit aspernatur aut odit aut fugi sed quia consequu.</p><svg class="card__go" viewBox="0 0 16 16"><circle cx="8" cy="8" r="7.3" fill="none" stroke="#c4976a" stroke-width=".9"/><path d="M7 5l3 3-3 3" fill="none" stroke="#c4976a" stroke-width=".9"/></svg></div>
      <div class="card"><div class="card__icon" role="img" aria-label="Insurance document icon"></div><h3 class="card__title">Insurance claims</h3><p class="card__text">Nemo enim ipsam voluptatem quia voluptas sit aspernatur aut odit aut fugi sed quia consequu.</p><svg class="card__go" viewBox="0 0 16 16"><circle cx="8" cy="8" r="7.3" fill="none" stroke="#c4976a" stroke-width=".9"/><path d="M7 5l3 3-3 3" fill="none" stroke="#c4976a" stroke-width=".9"/></svg></div>
      <div class="card"><div class="card__icon" role="img" aria-label="Hand holding money icon"></div><h3 class="card__title">Premises liability</h3><p class="card__text">Nemo enim ipsam voluptatem quia voluptas sit aspernatur aut odit aut fugi sed quia consequu.</p><svg class="card__go" viewBox="0 0 16 16"><circle cx="8" cy="8" r="7.3" fill="none" stroke="#c4976a" stroke-width=".9"/><path d="M7 5l3 3-3 3" fill="none" stroke="#c4976a" stroke-width=".9"/></svg></div>
    </div>
  </section>

  <section class="section remote" style="height:172px">
    <div class="abs remote__card">
      <div class="remote__body">
        <h2 class="abs heading remote__title">100% Remote</h2>
        <p class="abs remote__text">Jma veniam, quis nostrum exercitationem der ulm corporis susc ut aliquid ex ea commodi consdeequ atu saum iure reprehenderit.</p>
        <div class="abs feature" style="top:53px"><span class="feature__ring"><svg width="9" height="7" viewBox="0 0 18 14"><rect x="3" y="1" width="12" height="8" fill="none" stroke="#fff" stroke-width="1.4"/><path d="M1 12h16" stroke="#fff" stroke-width="1.6"/></svg></span><span>Private<br>online meetings</span></div>
        <div class="abs feature" style="top:78px"><span class="feature__ring"><svg width="8" height="8" viewBox="0 0 16 16"><rect x="1.5" y="3" width="11" height="11" rx="1.5" fill="none" stroke="#fff" stroke-width="1.4"/><path d="M6 10l1-3 6-6 2 2-6 6z" fill="none" stroke="#fff" stroke-width="1.4"/></svg></span><span>Signing<br>portals</span></div>
        <a class="btn">Contact us</a>
      </div>
      <div class="remote__photo" role="img" aria-label="Woman working on a laptop"></div>
    </div>
  </section>

  <section class="section reviews">
    <h2 class="abs heading reviews__title">Client Reviews</h2>
    <p class="abs reviews__quote">“ Lorem ipsum dolor sit amet, consectetur adipiscing elit, sed do eiusmod tempor incidi dunt ut labore et dolore magna aliqua. Ut enim ad minim veniam, quis nostrud exercita tion ullamco laboris nisi ut aliquip ex ea commodo consequat. Duis aute irure dolor in reprehenderit in voluptate velit esse cillum dolore eu fug ”</p>
    <p class="abs reviews__name">- LIORA</p>
    <svg class="abs arrow" style="left:67px" viewBox="0 0 16 16"><circle cx="8" cy="8" r="7.3" fill="none" stroke="#c4976a" stroke-width=".9"/><path d="M9 5L6 8l3 3" fill="none" stroke="#c4976a" stroke-width=".9"/></svg>
    <svg class="abs arrow" style="left:194px" viewBox="0 0 16 16"><circle cx="8" cy="8" r="7.3" fill="none" stroke="#c4976a" stroke-width=".9"/><path d="M7 5l3 3-3 3" fill="none" stroke="#c4976a" stroke-width=".9"/></svg>
    <div class="abs reviews__video" role="img" aria-label="Video testimonial from a client">
      <svg class="abs play" viewBox="0 0 20 20"><circle cx="10" cy="10" r="10" fill="#000"/><path d="M8 6l6 4-6 4z" fill="#fff"/></svg>
    </div>
  </section>

  <section class="section contact" style="height:167px">
    <div class="abs contact__card">
      <div class="contact__map" role="img" aria-label="Map of Florida"></div>
      <form class="contact__form">
        <h2 class="abs heading contact__title">Get In Touch</h2>
        <div class="field" style="left:10px;top:31px;width:58px;height:10px">First Name</div>
        <div class="field" style="left:71px;top:31px;width:58px;height:10px">Last Name</div>
        <div class="field" style="left:10px;top:46px;width:58px;height:10px">Email</div>
        <div class="field" style="left:71px;top:46px;width:58px;height:10px">Phone no.</div>
        <div class="field" style="left:10px;top:61px;width:119px;height:29px">Message</div>
        <a class="btn">Send</a>
      </form>
    </div>
  </section>

  <footer class="section footer">
    <span class="abs footer__mark"></span>
    <span class="abs footer__name">Telvarique Law</span>
    <div class="abs footer__col" style="left:149px"><h4>Quick Links</h4>Home<br>About Us<br>Contact Us<br>Services<br>Mailing Address<br>Testimonials<br>FAQs</div>
    <div class="abs footer__col" style="left:204px"><h4>Contact Info</h4>
      <div class="contact-row"><svg width="4" height="5" viewBox="0 0 8 10"><path d="M4 0a3.5 3.5 0 0 0-3.5 3.5C.5 6 4 10 4 10s3.5-4 3.5-6.5A3.5 3.5 0 0 0 4 0z" fill="#c4976a"/></svg>Florida, D.C</div>
      <div class="contact-row"><svg width="4" height="4" viewBox="0 0 10 10"><path d="M2 0l2 2.5-1 1.5a6 6 0 0 0 3 3l1.5-1L10 8l-1.5 2C4 10 0 6 0 1.5z" fill="#c4976a"/></svg>1 800 555 0142</div>
      <div class="contact-row"><svg width="5" height="4" viewBox="0 0 10 7"><rect width="10" height="7" fill="#c4976a"/><path d="M0 0l5 4 5-4" fill="none" stroke="#000" stroke-width=".8"/></svg>info@telvalaw.com</div>
    </div>
    <span class="abs footer__rule"></span>
    <p class="abs footer__copy">© Copyright 2025, TelvaLaw. All rights reserved.</p>
    <span class="abs social" style="left:223px"></span>
    <span class="abs social" style="left:235px"></span>
  </footer>
</main>

</body>
</html>
```